Kettles - Eggs For Sale Sign

Would like a graphic quality image of a EGGS FOR SALE SIGN ... am getting a local outdoor sign company to print the sign and attach it to a frame.

this is going to be outside by the gate to our farm ... would like the sign to "POP" ... DRAW ATTENTION ... as it were ... please.

I think we need it about 36”(w) x 30”(h) ... maybe 48”x36” ... not sure ... need about an extra 1 1/2” border around also so that we can frame this into a wooden frame ...

The color picture is similar to the pattern we like ... the fonts you are welcome to just blow us out of the water with ... we are not tied down to any particular font ... like the “WANTED” posters of old ... sorta.

Logo Text

Bramble Nook Acres

Colors

Requirements
Must have
• Some type of Fire Fly art ... not to modern ... not too comic book ...
Nice to have
• phone number
• call or text

```html
<!DOCTYPE html>
<html lang="en">
<head>
<meta charset="utf-8">
<title>Bramble Nook Acres – Eggs For Sale</title>
<link rel="stylesheet" href="https://fonts.googleapis.com/css2?family=Oswald:wght@500;600&family=Audiowide&family=Archivo+Black&display=swap">
<style>
  :root {
    --frame: #c4692a;
    --frame-dark: #8f4417;
    --frame-light: #dc8a48;
    --wood: #e6d8c6;
    --ink: #333132;
    --green: #0e8c4a;
    --red: #e8303a;
    --white: #ffffff;
    --oval-rim: #6fa0a8;
  }
  html, body {
    margin: 0;
    padding: 0;
    width: 1200px;
    height: 900px;
    overflow: hidden;
    background: var(--white);
  }
  .sign {
    display: block;
    width: 1200px;
    height: 900px;
  }
  .brand-name {
    font-family: "Oswald", sans-serif;
    font-weight: 600;
    font-size: 112px;
    fill: var(--ink);
  }
  .tagline {
    font-family: "Audiowide", sans-serif;
    font-size: 70px;
    fill: var(--green);
    stroke: var(--white);
    stroke-width: 10px;
    paint-order: stroke;
    stroke-linejoin: round;
  }
  .badge-text {
    font-family: "Oswald", sans-serif;
    font-weight: 500;
    font-size: 50px;
    fill: var(--white);
  }
  .product {
    font-family: "Oswald", sans-serif;
    font-weight: 600;
    font-size: 196px;
    fill: var(--ink);
  }
  .offer {
    font-family: "Archivo Black", sans-serif;
    font-size: 104px;
    fill: var(--red);
    stroke: var(--white);
    stroke-width: 12px;
    paint-order: stroke;
    stroke-linejoin: round;
  }
  .contact {
    font-family: "Archivo Black", sans-serif;
    font-size: 64px;
    fill: var(--ink);
    stroke: var(--white);
    stroke-width: 10px;
    paint-order: stroke;
    stroke-linejoin: round;
  }
</style>
</head>
<body>
<svg class="sign" viewBox="0 0 1200 900" xmlns="http://www.w3.org/2000/svg">
  <defs>
    <linearGradient id="woodTone" x1="0" y1="0" x2="0" y2="1">
      <stop offset="0" stop-color="#e3d4c1"/>
      <stop offset="0.5" stop-color="#e9ddcd"/>
      <stop offset="1" stop-color="#dccbb6"/>
    </linearGradient>
    <radialGradient id="ovalGlow" cx="0.5" cy="0.5" r="0.6">
      <stop offset="0" stop-color="#ffffff"/>
      <stop offset="1" stop-color="#d3e5ea"/>
    </radialGradient>
    <radialGradient id="ovalHalo" cx="0.5" cy="0.5" r="0.5">
      <stop offset="0.75" stop-color="#ffffff" stop-opacity="0.9"/>
      <stop offset="1" stop-color="#ffffff" stop-opacity="0"/>
    </radialGradient>
    <linearGradient id="hen" x1="0" y1="0" x2="0" y2="1">
      <stop offset="0" stop-color="#4a4646" stop-opacity="0.85"/>
      <stop offset="1" stop-color="#333132" stop-opacity="0.85"/>
    </linearGradient>
    <path id="taglineArc" d="M 115 385 Q 600 145 1090 385"/>
  </defs>

  <!-- frame -->
  <rect class="frame" x="0" y="0" width="1200" height="900" fill="var(--frame-dark)"/>
  <rect x="6" y="6" width="1188" height="888" fill="var(--frame)"/>
  <rect x="32" y="30" width="1136" height="840" fill="var(--frame-light)"/>

  <!-- weathered board background -->
  <rect class="board" role="img" aria-label="Weathered white-washed wooden planks"
        x="44" y="42" width="1112" height="816" fill="url(#woodTone)"/>

  <!-- brand name -->
  <g class="brand">
    <circle cx="1085" cy="118" r="18" fill="#f2a21c"/>
    <text class="brand-name" x="590" y="168" text-anchor="middle">Bramble Nook Acres</text>
  </g>

  <!-- arched tagline -->
  <text class="tagline">
    <textPath href="#taglineArc" startOffset="50%" text-anchor="middle">FRESH FROM THE FARM</textPath>
  </text>

  <!-- organic badge -->
  <rect class="badge" x="348" y="316" width="508" height="66" rx="33" fill="var(--ink)"/>
  <text class="badge-text" x="602" y="369" text-anchor="middle">ORGANIC FREE RANGE</text>

  <!-- product oval -->
  <ellipse cx="600" cy="538" rx="268" ry="148" fill="url(#ovalHalo)"/>
  <ellipse class="product-oval" cx="600" cy="538" rx="240" ry="124"
           fill="url(#ovalGlow)" stroke="var(--oval-rim)" stroke-width="5"/>
  <ellipse cx="600" cy="538" rx="232" ry="116" fill="none" stroke="var(--white)" stroke-width="3"/>
  <circle role="img" aria-label="Small flower ornament" cx="402" cy="538" r="18" fill="var(--ink)"/>
  <circle role="img" aria-label="Small flower ornament" cx="798" cy="538" r="18" fill="var(--ink)"/>
  <text class="product" x="600" y="612" text-anchor="middle"
        textLength="310" lengthAdjust="spacingAndGlyphs">EGGS</text>

  <!-- hen silhouettes -->
  <rect class="hen" role="img" aria-label="Silhouette of a hen facing right"
        x="76" y="432" width="182" height="208" rx="60" fill="url(#hen)"/>
  <rect class="hen" role="img" aria-label="Silhouette of a hen facing left"
        x="944" y="432" width="182" height="208" rx="60" fill="url(#hen)"/>

  <!-- offer -->
  <text class="offer" x="602" y="758" text-anchor="middle">FOR SALE</text>

  <!-- contact -->
  <text class="contact" x="600" y="836" text-anchor="middle">Call or Text : (555) 014-2387</text>
</svg>
</body>
</html>
```